Kestrelwood Restaurnt Lunch Menu Redesign:

We have two lunch special menus that need to be reformatted into a 4.25inx11in and need a graphics design update. Some menu items need to change and some descriptions need to updated. This new menu should double sided with the Main Dining Lunch Menu on the front side and Teppanyaki Lunch menu on the back.

Both menus should follow the same design formatting as the main dining lunch menu (font, sizing, ect.)

```html
<!DOCTYPE html>
<html lang="en">
<head>
<meta charset="utf-8">
<title>Kestrelwood Restaurnt – Lunch Menus</title>
<link href="https://fonts.googleapis.com/css2?family=Libre+Baskerville:ital,wght@0,700;1,700&family=Crimson+Pro:ital,wght@0,400;0,600;0,700;1,400;1,600&display=swap" rel="stylesheet">
<style>
:root{
  --backdrop:#ececec;
  --paper:#ffffff;
  --ink:#111111;
  --ink-soft:#2e2e2e;
  --ink-muted:#444444;
  --ornament-top:#f4f4f4;
  --ornament-bottom:#dcdcdc;
}
*{margin:0;padding:0;box-sizing:border-box}
html,body{width:1128px;height:1200px;overflow:hidden;background:var(--backdrop)}
body{position:relative;font-family:"Crimson Pro",Georgia,serif;color:var(--ink)}
.menu-card{position:absolute;top:18px;width:450px;height:1164px;background:var(--paper);box-shadow:0 3px 10px rgba(0,0,0,.18)}
.menu-card--dining{left:96px}
.menu-card--teppanyaki{left:583px}
.menu-card > *{position:absolute;left:0;right:0}
.card-title{font-family:"Libre Baskerville",Georgia,serif;font-weight:700;font-size:31px;line-height:40px;text-align:center;color:var(--ink)}
.card-subtitle{font-family:"Libre Baskerville",Georgia,serif;font-style:italic;font-weight:700;font-size:15px;line-height:20px;text-align:center}
.section-title{font-family:"Libre Baskerville",Georgia,serif;font-weight:700;font-size:27px;line-height:36px;text-align:center}
.section-note{font-style:italic;font-size:14px;line-height:18px;text-align:center;color:var(--ink-soft)}
.item{left:23px;right:30px;display:flex;justify-content:space-between;font-size:15.5px;line-height:20px}
.item-name{font-weight:700}
.item-name em{font-weight:400;font-size:14px}
.item-desc{display:block;font-weight:400;font-style:italic;font-size:14px;line-height:17px;padding-left:12px}
.item-price{font-size:17px}
.sushi-row{left:23px;right:10px;display:grid;grid-template-columns:231px 1fr;font-size:15.5px;line-height:20px}
.sushi-row b{font-weight:700}
.sushi-row em{font-size:14px;color:var(--ink-soft)}
.raw-note{left:23px;font-style:italic;font-size:14px;line-height:18px;color:var(--ink-soft)}
.tepp-row{left:27px;right:20px;display:flex;justify-content:space-between;font-size:15.5px;line-height:22px;color:var(--ink-soft)}
.tepp-row .item-price{color:var(--ink)}
.age-title{font-family:"Libre Baskerville",Georgia,serif;font-style:italic;font-weight:700;font-size:19px;line-height:30px;text-align:center}
.sunrise{left:64px;right:64px;height:97px;background:linear-gradient(180deg,var(--ornament-top),var(--ornament-bottom));border-radius:4px}
.footer-note{font-size:13px;line-height:16px;text-align:center}
.footer-fine{font-size:11px;line-height:14px;text-align:center}
</style>
</head>
<body>

<section class="menu-card menu-card--dining" aria-label="Kestrelwood Restaurnt main dining lunch specials">
  <h1 class="card-title" style="top:41px">Lunch Specials</h1>
  <p class="card-subtitle" style="top:85px">Served Daily 11AM - 3PM</p>

  <h2 class="section-title" style="top:132px">Sandwiches</h2>
  <p class="section-note" style="top:176px">Served with Choice of Miso Soup or House Salad &amp; Potato Chips</p>
  <div class="item" style="top:200px"><span class="item-name">Fried Breaded Calamari Steak<span class="item-desc">with Tomato, Lettuce, Onion &amp; House Tartar Sauce</span></span><span class="item-price">$16</span></div>
  <div class="item" style="top:243px"><span class="item-name">California Chicken Club<span class="item-desc">with Bacon, Tomato, Lettuce, Avocado &amp; 1000 Island</span></span><span class="item-price">$16</span></div>
  <div class="item" style="top:286px"><span class="item-name">Hamburger<span class="item-desc">with Tomato, Lettuce, Onion &amp; 1000 Island</span></span><span class="item-price">$18</span></div>

  <h2 class="section-title" style="top:341px">Sushi Specials</h2>
  <p class="section-note" style="top:385px">Please Select 4 of the followings for $ 16</p>
  <p class="section-note" style="top:412px">Served with a 4-piece California Roll &amp; Miso Soup or House Salad</p>
  <div class="sushi-row" style="top:436px"><span><b>*Hamachi</b> - <em>Yellowtail Amberjack</em></span><span><b>*Maguro</b> - <em>Yellow fin Tuna</em></span></div>
  <div class="sushi-row" style="top:462px"><span><b>*Hotate</b> - <em>Scallop</em></span><span><b>*Smoked Salmon</b></span></div>
  <div class="sushi-row" style="top:488px"><span><b>*Ika</b> - <em>Squid</em></span><span></span></div>
  <div class="sushi-row" style="top:515px"><span><b>*Ikura</b> - <em>Salmon Roe</em></span><span><b>Tako</b> - <em>Octopus</em></span></div>
  <div class="sushi-row" style="top:541px"><span><b>*Saba</b> - <em>Mackerel</em></span><span><b>Unagi</b> - <em>BBQ Eel</em></span></div>
  <div class="sushi-row" style="top:566px"><span><b>*Sake</b> - <em>Salmon</em></span><span><b>Ebi</b> - <em>Shrimp</em></span></div>
  <div class="sushi-row" style="top:593px"><span><b>*Escolar</b> - <em>Butterfish</em></span><span><b>Ahi</b> - <em>Seared Yellowfin</em></span></div>
  <div class="sushi-row" style="top:618px"><span><b>*Albacore</b> - <em>White Tuna</em></span><span><b>Ahi</b> - <em>Seared Yellowfin</em></span></div>
  <p class="raw-note" style="top:644px">*Served Raw</p>

  <h2 class="section-title" style="top:680px">Main Courses</h2>
  <p class="section-note" style="top:724px">Served with Steamed Rice &amp; Choice of Miso Soup or Garden Salad.<br>Upgrade to Fried Rice for $4</p>
  <div class="item" style="top:765px"><span class="item-name">Organic Tofu Teriyaki <em>- Served Grilled or Tempura Fried</em></span><span class="item-price">$14</span></div>
  <div class="item" style="top:791px"><span class="item-name">Chicken Teriyaki</span><span class="item-price">$16</span></div>
  <div class="item" style="top:816px"><span class="item-name">Spicy Chicken Teriyaki</span><span class="item-price">$16</span></div>
  <div class="item" style="top:842px"><span class="item-name">Beef Teriyaki</span><span class="item-price">$16</span></div>
  <div class="item" style="top:866px"><span class="item-name">Spicy Beef Teriyaki</span><span class="item-price">$16</span></div>
  <div class="item" style="top:892px"><span class="item-name">Chicken Katsu <em>- Breaded Chicken Breast</em></span><span class="item-price">$15</span></div>
  <div class="item" style="top:918px"><span class="item-name">Katsu Don <em>- Fried Chicken Breast, Egg &amp; Onion over Rice</em></span><span class="item-price">$16</span></div>
  <div class="item" style="top:943px"><span class="item-name">Unagi Don <em>- BBQ Eel over Rice</em></span><span class="item-price">$19</span></div>
  <div class="item" style="top:969px"><span class="item-name">Shrimp &amp; Vegetable Tempura</span><span class="item-price">$16</span></div>

  <div class="sunrise" style="top:1001px" role="img" aria-label="Line-drawn rising sun over a horizon line"></div>
  <p class="footer-note" style="top:1117px">20% gratuity added to parties of 6 or more.</p>
  <p class="footer-fine" style="top:1134px">Consuming raw or undercooked food may increase your risk of foodborne illness</p>
</section>

<section class="menu-card menu-card--teppanyaki" aria-label="Kestrelwood Restaurnt teppanyaki lunch special">
  <h1 class="card-title" style="top:36px">Teppanyaki Lunch Special</h1>
  <p class="card-subtitle" style="top:85px">Available until 11AM - 2:30PM</p>
  <p class="section-note" style="top:115px">Served with Miso Soup or Salad, Choice of Rice &amp; Vegetables</p>

  <div class="tepp-row" style="top:161px"><span>Hibachi Chicken</span><span class="item-price">$18</span></div>
  <div class="tepp-row" style="top:192px"><span>Hibachi Shrimp</span><span class="item-price">$19</span></div>
  <div class="tepp-row" style="top:224px"><span>Hibachi New York Steak</span><span class="item-price">$20</span></div>
  <div class="tepp-row" style="top:255px"><span>Hibachi Salmon</span><span class="item-price">$20</span></div>
  <div class="tepp-row" style="top:286px"><span>Teriyaki Beef</span><span class="item-price">$19</span></div>
  <div class="tepp-row" style="top:318px"><span>Hibachi Scallop</span><span class="item-price">$20</span></div>
  <div class="tepp-row" style="top:349px"><span>Chicken and Shrimp</span><span class="item-price">$21</span></div>
  <div class="tepp-row" style="top:380px"><span>Scallop and Shrimp</span><span class="item-price">$22</span></div>
  <div class="tepp-row" style="top:411px"><span>New York Steak and Chicken</span><span class="item-price">$22</span></div>
  <div class="tepp-row" style="top:443px"><span>New York Steak and Shrimp</span><span class="item-price">$23</span></div>
  <div class="tepp-row" style="top:474px"><span>New York Steak and Scallop</span><span class="item-price">$24</span></div>
  <div class="tepp-row" style="top:505px"><span>Filet Mignon</span><span class="item-price">$23</span></div>
  <div class="tepp-row" style="top:537px"><span>Filet Mignon and Chicken</span><span class="item-price">$25</span></div>
  <div class="tepp-row" style="top:568px"><span>Filet Mignon and Shrimp</span><span class="item-price">$26</span></div>
  <div class="tepp-row" style="top:599px"><span>Filet Mignon and Scallop</span><span class="item-price">$27</span></div>

  <h2 class="age-title" style="top:680px">Ages 12 and Under ~ Ages 65 and Older</h2>
  <p class="section-note" style="top:716px">Served with Miso Soup or Salad, Choice of Rice &amp; Vegetables</p>
  <div class="tepp-row" style="top:763px"><span>Hibachi Chicken</span><span class="item-price">$15</span></div>
  <div class="tepp-row" style="top:794px"><span>Hibachi Shrimp</span><span class="item-price">$16</span></div>
  <div class="tepp-row" style="top:826px"><span>Hibachi Scallop</span><span class="item-price">$18</span></div>
  <div class="tepp-row" style="top:857px"><span>Hibachi New York Steak</span><span class="item-price">$18</span></div>
  <div class="tepp-row" style="top:888px"><span>Teriyaki Beef</span><span class="item-price">$16</span></div>

  <div class="sunrise" style="top:1001px" role="img" aria-label="Line-drawn rising sun over a horizon line"></div>
  <p class="footer-note" style="top:1117px">20% gratuity added to parties of 6 or more.</p>
  <p class="footer-fine" style="top:1134px">Consuming raw or undercooked food may increase your risk of foodborne illness</p>
</section>

</body>
</html>
```